Harbor of Mercy - Team of Rabbis and Doctors Helping Families Dealing with Illness

The Harbor of Mercy is an organization that accompanies families dealing with severe illnesses of a family member. A team of rabbis and doctors provide support and real-time responses to these families.
The site theme is medicine and law, but the target market is religious Jewish families in crisis. Thus, the site design needs to combine:
- professional, conservative, serious
- spiritual
- warm hug

Target Market(s)

religious families suffering a health crisis

Industry/Entity Type

Non-profit organization

Number of Pages Required

1 page

Font styles to use
Sans Serif

Requirements
Must have
• Final design in PSD format. List of fonts used, colors used and link/button colors used in the design.

```html
<!DOCTYPE html>
<html lang="en">
<head>
<meta charset="utf-8">
<title>Harbor of Mercy</title>
<link href="https://fonts.googleapis.com/css2?family=Montserrat:wght@400;500;600;700;800&display=swap" rel="stylesheet">
<style>
:root{
  --teal:#4bb5b0;
  --teal-dark:#1a5a57;
  --teal-band:#23706d;
  --teal-foot:#1e6865;
  --orange:#f5a53a;
  --orange-deep:#ef8b2c;
  --ink:#4a4a4a;
  --muted:#6b6b6b;
  --hero-bg:#eeeeee;
  --beige:#f4efe8;
  --soft:#eef1f3;
  --line:#d9dde0;
  --white:#ffffff;
}
*{box-sizing:border-box;margin:0;padding:0}
html,body{width:1200px;height:4370px;overflow:hidden}
body{position:relative;background:var(--white);font-family:"Montserrat",sans-serif;color:var(--ink)}
.abs{position:absolute}
.heading{font-weight:700;color:var(--teal-dark);letter-spacing:1.5px;font-size:30px;text-transform:uppercase;white-space:nowrap}
.eyebrow{font-size:12px;color:var(--teal);letter-spacing:1px;text-transform:uppercase;font-weight:500}
.accent-rule{position:absolute;height:2px;background:var(--orange)}
.btn{position:absolute;display:flex;align-items:center;justify-content:center;border-radius:30px;color:var(--white);font-weight:700;text-transform:uppercase}
.photo{position:absolute}

/* top bar */
.topbar{left:0;top:0;width:1200px;height:30px;background:var(--teal-band);color:var(--white);font-size:13px;font-weight:600}
.topbar span{position:absolute;top:7px;display:flex;align-items:center;gap:6px}
.topbar i{position:absolute;top:0;width:1px;height:30px;background:rgba(255,255,255,.35)}
/* nav */
.nav a{position:absolute;top:75px;font-size:14px;color:#333;text-decoration:none}
.nav .active{color:var(--orange-deep)}
.logo-name{font-weight:700;color:var(--teal-dark);font-size:20px;display:flex;align-items:center;gap:8px;white-space:nowrap}
.logo-name b{width:14px;height:14px;border-radius:50%;background:var(--teal);display:inline-block}

/* hero */
.hero-bg{left:0;top:114px;width:1200px;height:574px;background:var(--hero-bg);border-bottom-left-radius:200px}
.hero-title{left:107px;top:248px;font-size:35px;line-height:44px;font-weight:700;color:var(--teal-dark);letter-spacing:1.5px}
.hero-title em{font-style:normal;background:var(--orange);color:var(--white);padding:0 10px;border-radius:6px}
.hero-text{left:110px;top:390px;width:450px;font-size:16.5px;line-height:26px;color:var(--muted)}
.slides span{position:absolute;top:468px;font-size:16px;color:var(--teal-dark);width:46px;text-align:center;padding-bottom:8px;border-bottom:2px solid var(--line)}
.slides .on{border-color:var(--orange-deep);color:var(--orange-deep)}

/* about */
.about-text{left:658px;width:468px;font-size:14.5px;line-height:23px;color:#555}

/* morals */
.morals-bg{left:0;top:1252px;width:1200px;height:515px;background:var(--beige)}

/* service cards */
.card{position:absolute;top:1838px;width:236px;height:334px;border:1px solid var(--line);background:var(--white)}
.card .photo{left:0;top:0;width:234px;height:165px}
.card h3{position:absolute;left:26px;top:182px;font-size:15px;letter-spacing:1.5px;color:var(--teal-dark);font-weight:600;display:flex;align-items:center;gap:8px}
.card h3:after{content:"";width:28px;height:1px;background:var(--teal)}
.card p{position:absolute;left:26px;top:210px;width:192px;font-size:10px;line-height:17px;color:#666}
.card .btn{left:24px;top:285px;width:120px;height:34px;background:var(--teal);font-size:9.5px}

/* testimonials */
.testi-bg{left:0;top:2245px;width:1200px;height:504px;background:var(--soft);border-top-right-radius:140px;border-bottom-left-radius:140px}
.quote{position:absolute;top:2427px;width:444px;height:249px;background:var(--white);border:1px solid var(--line);border-radius:10px}
.quote .avatar{position:absolute;left:28px;top:30px;width:52px;height:52px;border-radius:50%;background:linear-gradient(135deg,#d7b49a,#7b8b8e)}
.quote h4{position:absolute;left:92px;top:38px;font-size:14px;color:#222;font-weight:700}
.quote .stars{position:absolute;left:92px;top:56px;color:var(--orange-deep);font-size:16px;letter-spacing:1px}
.quote .mark{position:absolute;right:40px;top:24px;font-size:70px;line-height:70px;color:#f0b770;font-family:Georgia,serif}
.quote p{position:absolute;left:32px;top:110px;width:385px;font-size:14.5px;line-height:25px;color:#444}

/* news */
.news{position:absolute;top:2885px;width:305px;height:322px}
.news .photo{left:0;top:0;width:305px;height:200px}
.news .box{position:absolute;left:12px;top:170px;width:281px;height:152px;background:var(--white);border:1px solid var(--line);text-align:center}
.news .date{position:absolute;left:50%;top:-10px;transform:translateX(-50%);background:var(--orange);color:var(--white);font-size:9px;font-weight:600;padding:4px 12px;border-radius:10px;white-space:nowrap}
.news h4{margin-top:30px;font-size:14px;color:var(--teal-dark);font-weight:700}
.news p{margin:10px auto 0;width:255px;font-size:9.5px;line-height:17px;color:#777}
.news .more{display:block;margin-top:10px;font-size:10px;color:var(--orange-deep);font-weight:700;letter-spacing:1px}
.news.featured .box{background:var(--teal);border-color:var(--teal)}
.news.featured h4,.news.featured p,.news.featured .more{color:var(--white)}

/* contact */
.contact-bg{left:0;top:3280px;width:1200px;height:572px;background:var(--beige)}
.field{position:absolute;background:var(--white);border:1px solid #cfd3d6;font-size:13px;color:#555;padding:11px 16px}

/* newsletter & footer */
.news-band{left:0;top:3852px;width:1200px;height:139px;background:var(--teal-band)}
.footer{left:0;top:3991px;width:1200px;height:379px;background:var(--teal-foot);color:var(--white)}
.foot-title{position:absolute;color:var(--white);font-size:17px;font-weight:700;letter-spacing:1px}
.foot-title:after{content:"";display:block;width:34px;height:2px;background:var(--white);margin-top:9px}
.foot-links span{position:absolute;font-size:13px;color:#e4f1f0}
.social{position:absolute;top:4171px;width:42px;height:42px;border-radius:50%;background:var(--teal);display:flex;align-items:center;justify-content:center}
</style>
</head>
<body>

<!-- top bar -->
<div class="abs topbar">
  <span style="left:120px">
    <svg width="13" height="13" viewBox="0 0 13 13"><circle cx="5.5" cy="5.5" r="4" fill="none" stroke="#fff" stroke-width="1.6"/><line x1="8.5" y1="8.5" x2="12" y2="12" stroke="#fff" stroke-width="1.6"/></svg>Search</span>
  <i style="left:232px"></i>
  <span style="left:282px"><svg width="14" height="14"><circle cx="7" cy="7" r="6" fill="#fff"/></svg>Community</span>
  <i style="left:425px"></i>
  <span style="left:465px">
    <svg width="13" height="13" viewBox="0 0 24 24"><path d="M6 2l4 5-2 3a12 12 0 006 6l3-2 5 4-3 4C10 22 2 14 2 5z" fill="none" stroke="#fff" stroke-width="2.2"/></svg>Contact</span>
  <i style="left:596px"></i>
  <span style="left:626px"><svg width="16" height="16"><circle cx="8" cy="8" r="6.5" fill="none" stroke="#fff" stroke-width="1.5"/><text x="8" y="11" font-size="7" fill="#fff" text-anchor="middle" font-family="Montserrat,sans-serif">24</text></svg>Hotline</span>
  <i style="left:735px"></i>
  <span style="left:772px">
    <svg width="14" height="16" viewBox="0 0 14 16"><path d="M7 15s6-6 6-9A6 6 0 001 6c0 3 6 9 6 9z" fill="none" stroke="#fff" stroke-width="1.5"/></svg>Dedication 2</span>
  <i style="left:910px"></i>
  <span style="left:950px">
    <svg width="16" height="14" viewBox="0 0 16 14"><path d="M8 13S1 8.5 1 4.5A3.5 3.5 0 018 3a3.5 3.5 0 017 1.5C15 8.5 8 13 8 13z" fill="none" stroke="#fff" stroke-width="1.5"/></svg>Dedication 1</span>
</div>

<!-- nav -->
<nav class="nav">
  <a class="active" style="left:131px">Home</a>
  <div class="abs" style="left:124px;top:111px;width:62px;height:2px;background:var(--orange-deep)"></div>
  <a style="left:218px">About Us</a>
  <a style="left:325px">Courses</a>
  <a style="left:427px">Conferences</a>
  <a style="left:563px">News</a>
  <a style="left:645px">Resources</a>
  <a style="left:763px">Contact</a>
</nav>
<div class="abs logo-name" style="left:900px;top:70px"><b></b>Harbor of Mercy</div>

<!-- hero -->
<div class="abs hero-bg"></div>
<div class="photo" role="img" aria-label="Nurse in teal scrubs caring for a smiling elderly woman in a wheelchair" style="left:611px;top:114px;width:589px;height:574px;background:linear-gradient(90deg,#eeeeee 0%,#d9dcd9 25%,#8fc6c8 55%,#c9c3bf 80%,#e4e1de 100%)"></div>
<h1 class="abs hero-title">SHOULD <em>MORPHINE</em><br>BE GIVEN TO<br>THE PATIENT?</h1>
<p class="abs hero-text">Lorem ipsum dolor sit amet consectetur adipiscing elit sed do eiusmod tempor incididunt</p>
<div class="slides"><span class="on" style="left:111px">01</span><span style="left:174px">02</span><span style="left:228px">03</span></div>

<!-- about -->
<svg class="abs" style="left:97px;top:801px" width="280" height="366"><polygon points="0,0 280,0 168,366 0,366" fill="var(--teal)"/></svg>
<div class="photo" role="img" aria-label="Doctor reviewing a tablet with a young woman beside a window" style="left:114px;top:820px;width:477px;height:323px;background:linear-gradient(120deg,#8a8d88,#c9cbc7 45%,#b3a89b 75%,#7f8a7c)"></div>
<svg class="abs" style="left:328px;top:936px" width="60" height="60"><circle cx="30" cy="30" r="26" fill="none" stroke="#fff" stroke-width="3"/><polygon points="24,18 24,42 42,30" fill="#fff"/></svg>
<div class="abs" style="left:306px;top:1004px;font-size:15px;letter-spacing:2px;color:#fff">PLAY VIDEO</div>

<div class="abs eyebrow" style="left:658px;top:807px">Who we are</div>
<h2 class="abs heading" style="left:658px;top:824px">About Us</h2>
<div class="accent-rule" style="left:846px;top:845px;width:70px"></div>
<p class="abs about-text" style="top:888px">Lorem ipsum dolor sit amet, consectetur adipiscing elit, sed do eiusmod tempor incididunt ut labore et dolore magna aliqua. Quis ipsum suspendisse ultrices gravida. Risus commodo viverra maecenas accumsan lacus vel facilisis.</p>
<p class="abs about-text" style="top:1008px">Lorem ipsum dolor sit amet, consectetur adipiscing elit, sed do eiusmod tempor incididunt ut labore et nt ut labore et dolore magna aliqua. Quis ipsum suspendisse</p>
<div class="btn" style="left:658px;top:1105px;width:177px;height:51px;background:var(--orange);font-size:14px">Learn more</div>

<!-- morals -->
<div class="abs morals-bg"></div>
<div class="photo" role="img" aria-label="Doctor attending a smiling patient in a hospital bed" style="left:614px;top:1252px;width:586px;height:515px;border-top-left-radius:130px;background:linear-gradient(110deg,#e7ecef,#c8d2d8 40%,#9fb4c7 70%,#dfe3e6)"></div>
<div class="abs eyebrow" style="left:116px;top:1331px">Our morals</div>
<h2 class="abs heading" style="left:117px;top:1350px">More Moral Issues</h2>
<div class="accent-rule" style="left:478px;top:1371px;width:66px"></div>
<svg class="abs" style="left:106px;top:1412px" width="88" height="88"><circle cx="44" cy="44" r="41" fill="none" stroke="var(--teal)" stroke-width="2"/><circle cx="44" cy="44" r="33" fill="var(--teal)"/><circle cx="44" cy="33" r="6" fill="none" stroke="#fff" stroke-width="2"/><circle cx="33" cy="52" r="5" fill="none" stroke="#fff" stroke-width="2"/><circle cx="55" cy="52" r="5" fill="none" stroke="#fff" stroke-width="2"/></svg>
<p class="abs" style="left:206px;top:1424px;width:340px;font-size:14.5px;line-height:23px;font-weight:700;color:#222">Lorem ipsum dolor sit amet, consectetur adipiscing elit sed do eiusmod</p>
<p class="abs" style="left:209px;top:1478px;width:340px;font-size:14.5px;line-height:23px;color:#555">ut labore et dolore magna aliqua. Quis ipsum suspendisse ultrices gravida. Risus commodo viverra aecenas accumsan lacus vel facilisis. ut labore et dolore magna aliqua. Quis ipsum suspendisse ultrices gravida.</p>
<svg class="abs" style="left:205px;top:1624px" width="160" height="24"><polyline points="10,4 4,12 10,20" fill="none" stroke="var(--teal)" stroke-width="2"/><circle cx="40" cy="12" r="4" fill="var(--orange-deep)"/><circle cx="66" cy="12" r="3.5" fill="#bcdedb"/><circle cx="92" cy="12" r="3.5" fill="#bcdedb"/><circle cx="118" cy="12" r="3.5" fill="#bcdedb"/><polyline points="144,4 150,12 144,20" fill="none" stroke="var(--teal)" stroke-width="2"/></svg>

<!-- service cards -->
<div class="card" style="left:97px">
  <div class="photo" role="img" aria-label="Group of students in a course session" style="background:linear-gradient(135deg,#c8c2bc,#8c7f78 50%,#e0d4cf)"></div>
  <h3>COURSES</h3>
  <p>Lorem ipsum dolor sit amet, consectetur adipiscing elit sed do eiusmod tempotetur adipiscinLorem ipsum dolor sit amet consectetur</p>
  <div class="btn">Learn more</div>
</div>
<div class="card" style="left:350px">
  <div class="photo" role="img" aria-label="Audience seated at a conference with a presentation screen" style="background:linear-gradient(180deg,#4f7ca8,#2f4f6a 45%,#7a6655)"></div>
  <h3>CONFERENCES</h3>
  <p>Lorem ipsum dolor sit amet, consectetur adipiscing elit sed do eiusmod tempotetur adipiscinLorem ipsum dolor sit amet consectetur</p>
  <div class="btn">Learn more</div>
</div>
<div class="card" style="left:604px">
  <div class="photo" role="img" aria-label="Speaker at a podium giving a lecture on stage" style="background:linear-gradient(180deg,#ede9e3,#d6cdc3 55%,#7a4b2e)"></div>
  <h3>LECTURES</h3>
  <p>Lorem ipsum dolor sit amet, consectetur adipiscing elit sed do eiusmod tempotetur adipiscinLorem ipsum dolor sit amet consectetur</p>
  <div class="btn">Learn more</div>
</div>
<div class="card" style="left:857px">
  <div class="photo" role="img" aria-label="Medical staff member answering a hotline phone call" style="background:linear-gradient(135deg,#e6eaee,#6f8fb7 50%,#cfd6dc)"></div>
  <h3>HOTLINE 24/7</h3>
  <p>Lorem ipsum dolor sit amet, consectetur adipiscing elit sed do eiusmod tempotetur adipiscinLorem ipsum dolor sit amet consectetur</p>
  <div class="btn">Learn more</div>
</div>

<!-- testimonials -->
<div class="abs testi-bg"></div>
<div class="abs eyebrow" style="left:0;top:2299px;width:1200px;text-align:center">Testimonials</div>
<h2 class="abs heading" style="left:0;top:2317px;width:1200px;text-align:center">What People Says</h2>
<div class="accent-rule" style="left:525px;top:2383px;width:150px"></div>
<svg class="abs" style="left:94px;top:2538px" width="16" height="26"><polyline points="13,2 3,13 13,24" fill="none" stroke="var(--orange-deep)" stroke-width="3"/></svg>
<svg class="abs" style="left:1103px;top:2538px" width="16" height="26"><polyline points="3,2 13,13 3,24" fill="none" stroke="var(--orange-deep)" stroke-width="3"/></svg>
<div class="quote" style="left:153px">
  <div class="avatar" role="img" aria-label="Portrait of the reviewer"></div>
  <h4>Daniel Hartman</h4><div class="stars">★★★★★</div><div class="mark">”</div>
  <p>Lorem ipsum dolor sit amet, consectetur adipiscing elit, sed do eiusmod tempor incididunt ut labore et dolore magna aliqua. Ut enim ad minim veniam, quis nostrud exercitation ullamc</p>
</div>
<div class="quote" style="left:621px">
  <div class="avatar" role="img" aria-label="Portrait of the reviewer"></div>
  <h4>Daniel Hartman</h4><div class="stars">★★★★★</div><div class="mark">”</div>
  <p>Lorem ipsum dolor sit amet, consectetur adipiscing elit, sed do eiusmod tempor incididunt ut labore et dolore magna aliqua. Ut enim ad minim veniam, quis nostrud exercitation ullamc</p>
</div>

<!-- news -->
<div class="abs eyebrow" style="left:141px;top:2803px">Resources</div>
<h2 class="abs heading" style="left:141px;top:2820px">Latest News</h2>
<div class="accent-rule" style="left:374px;top:2841px;width:64px"></div>
<div class="news" style="left:141px">
  <div class="photo" role="img" aria-label="Doctor checking on a patient lying in bed" style="background:linear-gradient(120deg,#dfe5ea,#a9bfd3 50%,#e8e2dc)"></div>
  <div class="box"><span class="date">Nov 25, 2023</span><h4>Lorem ipsum dolor sit amet</h4><p>Sed ut perspiciatis unde omnis iste natus error sit voluptatem accusantium doloremque laudantiumSed ut perspiciatis unde omnis</p><span class="more">LEARN MORE</span></div>
</div>
<div class="news featured" style="left:470px">
  <div class="photo" role="img" aria-label="Doctor examining a patient on an examination table" style="background:linear-gradient(120deg,#8a9399,#d3d8dc 50%,#5e6d7c)"></div>
  <div class="box"><span class="date">Nov 10, 2023</span><h4>Lorem ipsum dolor sit amet</h4><p>Sed ut perspiciatis unde omnis iste natus error sit voluptatem accusantium doloremque laudantiumSed ut perspiciatis unde omnis</p><span class="more">LEARN MORE</span></div>
</div>
<div class="news" style="left:801px">
  <div class="photo" role="img" aria-label="Doctor comforting a smiling senior woman" style="background:linear-gradient(120deg,#e9ecee,#c4ccd2 50%,#7f9bb6)"></div>
  <div class="box"><span class="date">Nov 12, 2023</span><h4>Lorem ipsum dolor sit amet</h4><p>Sed ut perspiciatis unde omnis iste natus error sit voluptatem accusantium doloremque laudantiumSed ut perspiciatis unde omnis</p><span class="more">LEARN MORE</span></div>
</div>

<!-- contact -->
<div class="abs contact-bg"></div>
<svg class="abs" style="left:76px;top:3326px" width="476" height="476"><circle cx="238" cy="238" r="236" fill="none" stroke="#dedbd3" stroke-width="2"/></svg>
<div class="photo" role="img" aria-label="Doctor discussing notes on a tablet with a smiling woman" style="left:88px;top:3338px;width:452px;height:452px;border-radius:50%;background:radial-gradient(circle at 40% 45%,#f1d2b8,#c9a888 45%,#8d9aa8 80%)"></div>
<div class="abs eyebrow" style="left:614px;top:3367px">Get in touch</div>
<h2 class="abs heading" style="left:614px;top:3384px">Contact Us</h2>
<div class="accent-rule" style="left:828px;top:3405px;width:64px"></div>
<div class="field" style="left:614px;top:3447px;width:223px;height:41px">First Name</div>
<div class="field" style="left:845px;top:3447px;width:219px;height:41px">Last Name</div>
<div class="field" style="left:614px;top:3497px;width:223px;height:41px">Phone Number</div>
<div class="field" style="left:845px;top:3497px;width:219px;height:41px">Email address</div>
<div class="field" style="left:614px;top:3547px;width:450px;height:42px">Subject</div>
<div class="field" style="left:614px;top:3598px;width:450px;height:93px">Message</div>
<div class="btn" style="left:614px;top:3708px;width:188px;height:49px;background:var(--orange);font-size:15px;font-weight:500">Send message</div>

<!-- newsletter -->
<div class="abs news-band"></div>
<div class="abs" style="left:131px;top:3912px;font-size:20px;font-weight:700;letter-spacing:1.5px;color:#fff">SUBSCRIBE NEWSLETTER</div>
<div class="abs" style="left:516px;top:3898px;width:522px;height:58px;background:#fff;border:1px solid #e4e4e4"></div>
<svg class="abs" style="left:535px;top:3920px" width="20" height="15"><rect x="1" y="1" width="18" height="13" fill="none" stroke="var(--teal)" stroke-width="1.6"/><polyline points="1,1 10,8 19,1" fill="none" stroke="var(--teal)" stroke-width="1.6"/></svg>
<div class="abs" style="left:568px;top:3918px;font-size:14px;color:#444">E-mail address</div>
<div class="btn" style="left:896px;top:3904px;width:136px;height:46px;border-radius:0;background:linear-gradient(90deg,#f7b24e,#ef8b2c);font-size:12px">Subscribe ➤</div>

<!-- footer -->
<div class="abs footer"></div>
<div class="abs logo-name" style="left:132px;top:4090px;color:#fff;font-size:24px"><b style="background:#fff"></b>Harbor of Mercy</div>
<div class="social" aria-label="Share" style="left:183px">
  <svg width="18" height="18" viewBox="0 0 18 18"><circle cx="4" cy="9" r="2.3" fill="#fff"/><circle cx="14" cy="4" r="2.3" fill="#fff"/><circle cx="14" cy="14" r="2.3" fill="#fff"/><line x1="4" y1="9" x2="14" y2="4" stroke="#fff" stroke-width="1.5"/><line x1="4" y1="9" x2="14" y2="14" stroke="#fff" stroke-width="1.5"/></svg>
</div>
<div class="social" aria-label="Email" style="left:239px">
  <svg width="18" height="14"><rect x="1" y="1" width="16" height="12" fill="none" stroke="#fff" stroke-width="1.6"/><polyline points="1,1 9,7 17,1" fill="none" stroke="#fff" stroke-width="1.6"/></svg>
</div>
<div class="social" aria-label="Website" style="left:295px">
  <svg width="18" height="18" viewBox="0 0 18 18"><circle cx="9" cy="9" r="7.5" fill="none" stroke="#fff" stroke-width="1.5"/><ellipse cx="9" cy="9" rx="3.2" ry="7.5" fill="none" stroke="#fff" stroke-width="1.3"/><line x1="1.5" y1="9" x2="16.5" y2="9" stroke="#fff" stroke-width="1.3"/></svg>
</div>

<div class="foot-title" style="left:511px;top:4055px">QUICK LINKS</div>
<div class="foot-title" style="left:840px;top:4052px">CONTACT US</div>
<div class="foot-links">
  <span style="left:512px;top:4101px">About</span>
  <span style="left:512px;top:4131px">Our Services</span>
  <span style="left:512px;top:4160px">Courses</span>
  <span style="left:512px;top:4191px">Lectures</span>
  <span style="left:512px;top:4221px">News</span>
  <span style="left:675px;top:4102px">Testimonials</span>
  <span style="left:675px;top:4133px">Conference</span>
  <span style="left:675px;top:4163px">Blog</span>
  <span style="left:675px;top:4193px">Contact</span>
</div>
<svg class="abs" style="left:845px;top:4105px" width="24" height="24" viewBox="0 0 24 24"><path d="M6 2l4 5-2 3a12 12 0 006 6l3-2 5 4-3 4C10 22 2 14 2 5z" fill="none" stroke="#fff" stroke-width="1.6"/></svg>
<div class="abs" style="left:881px;top:4094px;font-size:13px;color:#fff;line-height:20px"><b>24/7 Hotline Service</b><br>(480) 555-0142</div>
<svg class="abs" style="left:846px;top:4163px" width="24" height="18"><rect x="1" y="1" width="22" height="16" fill="none" stroke="#fff" stroke-width="1.6"/><polyline points="1,1 12,10 23,1" fill="none" stroke="#fff" stroke-width="1.6"/></svg>
<div class="abs" style="left:881px;top:4154px;font-size:13px;color:#e4f1f0;line-height:20px">Email us at<br>info@harborofmercy.org</div>

<div class="abs" style="left:0;top:4299px;width:1200px;height:1px;background:rgba(255,255,255,.2)"></div>
<div class="abs" style="left:0;top:4326px;width:1200px;text-align:center;font-size:12px;color:#e4f1f0">© 2023 Harbor of Mercy All Rights Reserved</div>
<svg class="abs" style="left:1035px;top:4282px" width="44" height="44"><circle cx="22" cy="22" r="21" fill="var(--orange)"/><polyline points="14,22 22,14 30,22" fill="none" stroke="#fff" stroke-width="2"/><line x1="22" y1="14" x2="22" y2="31" stroke="#fff" stroke-width="2"/></svg>

</body>
</html>
```